One of Australia's fastest growing energy maintenance contractors needs a new website

www.panelbrite.com.au
Our business has evolved over the past years and now our website is no longer relevant.
We clean solar panels and we vacuum roof gutters.
We clean solar panels on the roofs of residential houses right up to billion dollar solar farms with in excess of 1 million panels. We offer thermal image testing and bird proofing for our residential and commercial clients and thermal drone imaging services for our solar farm clients.
We vacuum clean roof gutters (using a LoftSuk) on the residential house next door right up to enormous private and public schools, colleges, shopping centres, strat complexes and commercial buildings.
When first built our business had more of a domestic residential skew and the website reflected that. While that is still part of our core business we are now bidding on and have secured large government, commercial and infrastructure contracts and our new website needs to reflect our growth and our new business. We need a new site that it optimised for both desktop ad phone viewing as our latest figures showed that 73% of people visiting our site are on mobile phones. We have an extensive amount of data on Trekmetrics available as well as Bidlinks. Both that would also need integrating with the site along with a few other plugins such as Kembo Chat IQ, Friendwall etc along with SEO key words etc. We are also the winner and finalists over multiple years of the small business of the year awards and we like to proudly and prominently display those on our site.
We are looking for a new site with a modern professional feel / theme
There is a definitive break in our business between the solar Panel cleaning clients and the gutter cleaning clients so we would like a home page that begins with a simple choice:
Solar Panel Cleaning – Gutter Cleaning
With a professional full screen background image (we have hundreds to choose from) and along the bottom a small area with rights reserved etc, phone number etc (at some point in the future we will split these into two businesses but for now it’s what we have).
After that selection is made we would like a repeat of that same scenario but the selection is:
If it’s Solar Panel Cleaning
(new background image)
Government – Infrastructure – Commercial – Residential
If it’s Gutter Cleaning
(new background image)
Government – Strata – Commercial – Residential
After making those choices then onto the relevant pages with background images relevant to each sector and a them that suits (on the residential we would like to keep the link to our trekmetrics reviews) - We will provide copy / text for each relevant page.
Other than that, a menu inclusive of the above and:
Resellers Portal – we will provide a link to this from Kembo CRM)
Customer portal (we will supply a link to this from our booking system)
We also need a page for our Solar Resellers / Partners page but we will give them a link to this, it won’t be listed on the site.
Request a quote page (Again we will provide information from Kembo as this will be linked to the CRM)
Standard contact us page inclusive of phone numbers, address and fields supplied from CRM
Sydney – 02 7391 5084
Southern Highlands – 02 4863 1507
Goulburn – 02 4863 1507
Canberra – 02 6178 3045
Wollongong – 02 4239 7615
sales@panelbrite.com.au
Head Office - Ferndell NSW 2583
ABN: 48762093115
Responsive Design: Optimized for desktop and mobile (73% mobile visitors).
Fast Loading Speed: Optimized for performance.
Smooth Transition Animations: For service and category selection.
Sticky Contact Bar: Always accessible at the bottom of mobile screens for quick calls.
SEO Optimization: Focused on government tenders, large-scale commercial contracts, and infrastructure projects.
Integrations
Trekmetrics & Trekmetrics Bidlinks.
Kembo Chat IQ.
Friendwall Beacon.
SEO tools and keyword optimization.
Many many more images available if needed

```html
<!DOCTYPE html>
<html lang="en">
<head>
<meta charset="utf-8">
<title>Panelbrite – Choose a Service</title>
<link rel="stylesheet" href="https://fonts.googleapis.com/css2?family=Poppins:ital,wght@0,400;0,500;0,600;0,800;1,400&display=swap">
<style>
  :root {
    --solar-orange: #ffa000;
    --solar-glow: #ffb300;
    --gutter-blue: #17a3da;
    --gutter-sky: #2bb3e0;
    --ink: #111111;
    --white: #ffffff;
    --photo-solar-a: #5c6168;
    --photo-solar-b: #3f454d;
    --photo-gutter-a: #5a5e58;
    --photo-gutter-b: #3b404a;
  }
  * { box-sizing: border-box; margin: 0; padding: 0; }
  html, body { width: 1200px; height: 600px; overflow: hidden; }
  body { font-family: "Poppins", sans-serif; }

  .choice-screen { position: relative; width: 1200px; height: 600px; display: flex; overflow: hidden; }

  .service-panel { position: relative; width: 600px; height: 600px; overflow: hidden; }
  .service-panel--solar {
    background: radial-gradient(ellipse 260px 200px at 450px 200px, var(--solar-glow), transparent 70%), var(--solar-orange);
    color: var(--ink);
  }
  .service-panel--gutter {
    background: radial-gradient(ellipse 300px 200px at 420px 160px, var(--gutter-sky), transparent 70%), var(--gutter-blue);
    color: var(--white);
  }

  .service-photo { position: absolute; }
  .service-photo--solar {
    left: 270px; top: 280px; width: 330px; height: 320px;
    background: linear-gradient(180deg, var(--photo-solar-a), var(--photo-solar-b));
  }
  .service-photo--gutter {
    left: 300px; top: 250px; width: 300px; height: 350px;
    background: linear-gradient(180deg, var(--photo-gutter-a), var(--photo-gutter-b));
  }

  .service-copy { position: absolute; left: 64px; top: 130px; }
  .service-panel--gutter .service-copy { left: 662px; left: 62px; }

  .eyebrow { display: flex; align-items: center; gap: 8px; font-size: 12px; font-style: italic; font-weight: 400; }
  .eyebrow::before { content: ""; width: 26px; height: 1px; background: currentColor; }

  .service-title { margin-top: 14px; font-size: 46px; font-weight: 800; line-height: 53px; letter-spacing: -0.5px; text-transform: uppercase; }
  .service-panel--gutter .service-title { margin-top: 2px; }

  .learn-more {
    position: absolute; top: 288px; left: 64px;
    width: 178px; height: 44px; border: 2px solid currentColor; border-radius: 22px;
    display: flex; align-items: center; justify-content: center; gap: 12px;
    font-size: 15px; font-weight: 500; color: inherit; text-decoration: none;
  }
  .service-panel--gutter .learn-more { left: 62px; }
  .learn-more svg { width: 18px; height: 12px; }

  .brand-tab {
    position: absolute; left: 64px; top: 0; width: 77px; height: 77px;
    background: var(--white); border-radius: 0 0 38px 38px;
    display: flex; flex-direction: column; align-items: center; justify-content: center; gap: 4px;
    color: var(--gutter-blue); font-size: 11px; font-weight: 600;
  }
  .brand-tab .brand-dot { width: 14px; height: 14px; background: var(--gutter-blue); }

  .contact-email {
    position: absolute; right: 64px; top: 30px; display: flex; align-items: center; gap: 8px;
    font-size: 12.5px; color: var(--white); text-decoration: none;
  }
  .contact-email svg { width: 12px; height: 12px; }

  .site-footer { position: absolute; left: 64px; bottom: 22px; font-size: 11px; color: var(--ink); }
  .footer-rule { position: absolute; left: 180px; width: 840px; top: 569px; height: 1px; background: rgba(255,255,255,0.35); }
</style>
</head>
<body>
<main class="choice-screen">
  <section class="service-panel service-panel--solar">
    <div class="service-photo service-photo--solar" role="img" aria-label="Photo of a house roof fitted with solar panels being washed"></div>
    <div class="service-copy">
      <p class="eyebrow">LOREM IPSUM</p>
      <h2 class="service-title">Solar Panel<br>Cleaning</h2>
    </div>
    <a class="learn-more" href="#solar">LEARN MORE
      <svg viewBox="0 0 18 12" fill="none" stroke="currentColor" stroke-width="2" stroke-linecap="round" stroke-linejoin="round"><path d="M1 6h15M11 1l5 5-5 5"/></svg>
    </a>
    <p class="site-footer">© Panelbrite 2025</p>
  </section>

  <section class="service-panel service-panel--gutter">
    <div class="service-photo service-photo--gutter" role="img" aria-label="Photo of a gutter vacuum hose clearing debris from a roof gutter"></div>
    <div class="service-copy">
      <p class="eyebrow">LOREM IPSUM</p>
      <h2 class="service-title">Gutter<br>Cleaning</h2>
    </div>
    <a class="learn-more" href="#gutter">LEARN MORE
      <svg viewBox="0 0 18 12" fill="none" stroke="currentColor" stroke-width="2" stroke-linecap="round" stroke-linejoin="round"><path d="M1 6h15M11 1l5 5-5 5"/></svg>
    </a>
    <a class="contact-email" href="mailto:sales@panelbrite.com.au">
      <svg viewBox="0 0 12 12" fill="none" stroke="currentColor" stroke-width="1.2" stroke-linejoin="round"><path d="M11 1L1 5l4 1.5L6.5 11 11 1zM5 6.5L11 1"/></svg>
      sales@panelbrite.com.au
    </a>
  </section>

  <div class="brand-tab"><span class="brand-dot"></span>Panelbrite</div>
  <div class="footer-rule"></div>
</main>
</body>
</html>
```